Contact Page for Design Number 58170946

I would like to request a "Contact Us" page for the site delivered in Design Number 58170946.

1) The page should be responsive on desktop, tablet and mobile phone.
2) The page should have the following fields:
- Name (text)
- Email address (text)
- Topic (list: Question, Complaint, Appreciation)
- Subject (text)
- Message (textarea)
- Send (button)
3) I would like to get the html and css code.
4) I need to know explicitly the changes done to the css of the final version of Design Number 58170946 required for the new "Contact Us" page.

```html
<!DOCTYPE html>
<html lang="en">
<head>
<meta charset="utf-8">
<title>Contact Us</title>
<link rel="stylesheet" href="https://fonts.googleapis.com/css2?family=Poppins:wght@400;600;700&display=swap">
<style>
  :root {
    --navy: #203459;
    --navy-deep: #1a2d52;
    --label: #0f1f45;
    --text: #333a45;
    --border: #dcdfe5;
    --white: #ffffff;
    --accent: #f04b4b;
    --accent-dark: #c93636;
  }
  * { box-sizing: border-box; margin: 0; padding: 0; }
  html, body {
    width: 1200px; height: 888px; overflow: hidden;
    background: var(--white);
    font-family: "Poppins", sans-serif;
  }
  .page { position: relative; width: 1200px; height: 888px; }
  .hero { position: absolute; left: 0; top: 0; width: 1200px; height: 220px; }
  .hero svg { display: block; }
  .hero-title {
    position: absolute; left: 0; right: 0; top: 60px;
    text-align: center; color: var(--white);
    font-weight: 700; font-size: 65px; line-height: 1; letter-spacing: 1px;
  }
  .contact-form { position: absolute; left: 214px; top: 0; width: 770px; }
  .field { position: absolute; }
  .field-label {
    display: block; color: var(--label);
    font-weight: 600; font-size: 27px; line-height: 1;
    margin-bottom: 12px;
  }
  .field-input {
    display: block; width: 100%; height: 64px;
    border: 1px solid var(--border); border-radius: 5px;
    background: var(--white);
    box-shadow: 0 4px 12px rgba(20, 30, 60, 0.07);
    padding: 0 26px;
    font-family: "Poppins", sans-serif; font-size: 25px; color: var(--text);
    outline: none; appearance: none;
  }
  .field-input::placeholder { color: var(--text); opacity: 1; }
  .field-select { position: relative; }
  .field-select .chevron { position: absolute; right: 22px; top: 29px; pointer-events: none; }
  .field-textarea { height: 185px; padding-top: 16px; resize: none; line-height: 1.3; }
  .f-name    { left: 0;   top: 265px; width: 378px; }
  .f-email   { left: 392px; top: 265px; width: 378px; }
  .f-topic   { left: 0;   top: 393px; width: 378px; }
  .f-subject { left: 392px; top: 393px; width: 378px; }
  .f-message { left: 0;   top: 524px; width: 770px; }
  .send-button {
    position: absolute; left: 299px; top: 773px;
    width: 172px; height: 70px; border: none; border-radius: 35px;
    background: var(--accent);
    box-shadow: 0 4px 0 var(--accent-dark);
    color: var(--white);
    font-family: "Poppins", sans-serif; font-weight: 700; font-size: 26px; letter-spacing: 1px;
  }
</style>
</head>
<body>
<main class="page">
  <header class="hero">
    <svg width="1200" height="220" viewBox="0 0 1200 220" role="img" aria-label="Navy header band with soft abstract background">
      <defs>
        <linearGradient id="hero-fill" x1="0" y1="0" x2="0" y2="1">
          <stop offset="0" stop-color="var(--navy-deep)"/>
          <stop offset="1" stop-color="var(--navy)"/>
        </linearGradient>
      </defs>
      <path d="M0 0 H1200 V116 Q600 310 0 102 Z" fill="url(#hero-fill)"/>
    </svg>
    <h1 class="hero-title">Contact Us</h1>
  </header>

  <form class="contact-form">
    <div class="field f-name">
      <label class="field-label" for="name">Name</label>
      <input class="field-input" id="name" type="text" placeholder="Enter Your Name">
    </div>
    <div class="field f-email">
      <label class="field-label" for="email">Email</label>
      <input class="field-input" id="email" type="text" placeholder="Enter Email Address">
    </div>
    <div class="field f-topic">
      <label class="field-label" for="topic">Topic</label>
      <div class="field-select">
        <select class="field-input" id="topic">
          <option>Question</option>
          <option>Complaint</option>
          <option>Appreciation</option>
        </select>
        <svg class="chevron" width="14" height="9" viewBox="0 0 14 9" aria-hidden="true">
          <path d="M1.5 1.5 L7 7 L12.5 1.5" fill="none" stroke="var(--label)" stroke-width="2.4" stroke-linecap="round" stroke-linejoin="round"/>
        </svg>
      </div>
    </div>
    <div class="field f-subject">
      <label class="field-label" for="subject">Subject</label>
      <input class="field-input" id="subject" type="text" placeholder="Enter Your Subject">
    </div>
    <div class="field f-message">
      <label class="field-label" for="message">Message</label>
      <textarea class="field-input field-textarea" id="message" placeholder="Type Your Messages..."></textarea>
    </div>
    <button class="send-button" type="button">SEND</button>
  </form>
</main>
</body>
</html>
```